A5 Personal trainer profile for corbell vitality

I need a A5 Landscape profile designed for the company I work for. Company name is Corbell Vitality. The profile is for personal trainers to let people know:

1. Brief description of themselves
2. Qualifications

A picture will be required on the right hand side of the profile. Corbell Vitality colours are green and white.

The Corbell Vitality Logo in the boarder of the example included must remain. We are looking for a clinical and professional design.

Industry/Entity Type

Health

```html
<!DOCTYPE html>
<html lang="en">
<head>
<meta charset="utf-8">
<title>Personal Trainer Profile – Corbell Vitality</title>
<link rel="stylesheet" href="https://fonts.googleapis.com/css2?family=Arimo:wght@400;700&family=Oswald:wght@600&family=Tinos&display=swap">
<style>
  :root {
    --brand-green: #3a9a1e;
    --text-green: #2f8f14;
    --frame-green: #22a01c;
    --accent-red: #e3161d;
    --ink: #1a1a1a;
    --wash-light: #eef8dc;
    --wash-mid: #d6efb0;
    --band-green: #b5e06a;
    --white: #ffffff;
  }
  * { box-sizing: border-box; margin: 0; padding: 0; }
  html, body { width: 1200px; height: 900px; overflow: hidden; background: var(--white); }
  .profile {
    position: relative;
    width: 1200px;
    height: 900px;
    overflow: hidden;
    background: var(--white);
  }
  .profile__backdrop { position: absolute; inset: 0; }

  .role-title {
    position: absolute; left: 63px; top: 36px;
    font: 400 40px/1 "Tinos", "Times New Roman", serif;
    color: var(--ink);
  }
  .trainer-name {
    position: absolute; left: 62px; top: 98px;
    font: 400 62px/1 "Tinos", "Times New Roman", serif;
    color: var(--accent-red);
    letter-spacing: 0.5px;
  }

  .section-band {
    position: absolute; left: 0; width: 360px; height: 48px;
    background: linear-gradient(90deg, var(--band-green) 0%, #d8f0a8 45%, rgba(255,255,255,0) 100%);
    display: flex; align-items: center; padding-left: 64px;
    font: 400 28px/1 "Tinos", "Times New Roman", serif;
    color: var(--accent-red);
  }
  .section-band--help { top: 198px; }
  .section-band--quals { top: 648px; }

  .tick-list { position: absolute; left: 24px; list-style: none; }
  .tick-list li {
    position: relative;
    padding-left: 40px;
    font: 400 24px/1 "Arimo", Arial, sans-serif;
    color: var(--text-green);
    letter-spacing: 0.2px;
  }
  .tick-list li svg { position: absolute; left: 0; top: 2px; width: 30px; height: 26px; }
  .tick-list--help { top: 275px; }
  .tick-list--help li { margin-bottom: 15px; }
  .tick-list--quals { top: 718px; }
  .tick-list--quals li { margin-bottom: 15px; padding-left: 42px; }

  .testimonial { position: absolute; left: 0; top: 470px; width: 1200px; text-align: center; }
  .testimonial__heading {
    font: 600 26px/1 "Oswald", "Arial Narrow", sans-serif;
    color: var(--accent-red);
    margin-bottom: 16px;
  }
  .testimonial__quote {
    font: 400 24px/42px "Tinos", "Times New Roman", serif;
    color: var(--text-green);
  }

  .portrait-frame {
    position: absolute; left: 826px; top: 17px;
    width: 360px; height: 394px;
    border: 7px solid var(--frame-green);
    background: var(--white);
    padding: 10px;
  }
  .portrait {
    width: 100%; height: 100%;
    background: linear-gradient(180deg, #f4f4f4 0%, #e6e6e6 35%, #9fd23a 75%, #7fc61e 100%);
  }

  .brand-mark {
    position: absolute; right: 8px; bottom: 6px;
    display: flex; align-items: center; gap: 6px;
    font: 700 26px/1 "Arimo", Arial, sans-serif;
    color: var(--brand-green);
  }
  .brand-mark__square { width: 20px; height: 20px; background: var(--brand-green); }
</style>
</head>
<body>
<main class="profile">
  <svg class="profile__backdrop" width="1200" height="900" viewBox="0 0 1200 900" aria-hidden="true">
    <defs>
      <linearGradient id="wash-top" x1="0" y1="0" x2="1" y2="0">
        <stop offset="0" stop-color="#dcf2b8"/>
        <stop offset="0.6" stop-color="#eef8dc"/>
        <stop offset="1" stop-color="#ffffff" stop-opacity="0"/>
      </linearGradient>
      <linearGradient id="wash-bottom" x1="0" y1="0" x2="1" y2="0">
        <stop offset="0" stop-color="#ffffff" stop-opacity="0"/>
        <stop offset="0.5" stop-color="#e4f5c6"/>
        <stop offset="1" stop-color="#c9ea8f"/>
      </linearGradient>
    </defs>
    <path d="M0 0 H520 C420 60 260 130 0 190 Z" fill="url(#wash-top)"/>
    <path d="M0 0 H360 C260 40 140 80 0 110 Z" fill="#e6f6cc" opacity="0.7"/>
    <path d="M0 900 C400 860 800 760 1200 560 V900 Z" fill="url(#wash-bottom)" opacity="0.8"/>
    <path d="M300 900 C700 870 1000 780 1200 680 V900 Z" fill="#d6efb0" opacity="0.6"/>
    <path d="M0 470 C300 640 700 660 1200 560" fill="none" stroke="#e3f4c8" stroke-width="30" opacity="0.6"/>
  </svg>

  <h1 class="role-title">Personal Trainer</h1>
  <h2 class="trainer-name">MARCUS OBENG</h2>

  <div class="section-band section-band--help">How I can help you?</div>
  <ul class="tick-list tick-list--help">
    <li><svg viewBox="0 0 30 26"><path d="M2 15 L11 24 C16 12 22 6 29 2" fill="none" stroke="#e3161d" stroke-width="2.4" stroke-linecap="round"/></svg>Reduce body fat and increase body definition.</li>
    <li><svg viewBox="0 0 30 26"><path d="M2 15 L11 24 C16 12 22 6 29 2" fill="none" stroke="#e3161d" stroke-width="2.4" stroke-linecap="round"/></svg>Increase stamina, improve agility and speed.</li>
    <li><svg viewBox="0 0 30 26"><path d="M2 15 L11 24 C16 12 22 6 29 2" fill="none" stroke="#e3161d" stroke-width="2.4" stroke-linecap="round"/></svg>Increase strength and size.</li>
    <li><svg viewBox="0 0 30 26"><path d="M2 15 L11 24 C16 12 22 6 29 2" fill="none" stroke="#e3161d" stroke-width="2.4" stroke-linecap="round"/></svg>Plyometric training and conditioning .</li>
    <li><svg viewBox="0 0 30 26"><path d="M2 15 L11 24 C16 12 22 6 29 2" fill="none" stroke="#e3161d" stroke-width="2.4" stroke-linecap="round"/></svg>Flexibility and core strength.</li>
  </ul>

  <div class="portrait-frame">
    <div class="portrait" role="img" aria-label="Portrait photo of the personal trainer in a green polo shirt"></div>
  </div>

  <section class="testimonial">
    <h3 class="testimonial__heading">What my clients say about me?</h3>
    <p class="testimonial__quote">“With Marcus my training is always challenging and fun. I don't remember a session to be boring or repetitive.<br>In short time I improved my core strength and flexibility. I can run 10k without stopping.<br>It is amazing improvement. " Laura Pennick.</p>
  </section>

  <div class="section-band section-band--quals">Qualifications</div>
  <ul class="tick-list tick-list--quals">
    <li><svg viewBox="0 0 30 26"><path d="M2 15 L11 24 C16 12 22 6 29 2" fill="none" stroke="#e3161d" stroke-width="2.4" stroke-linecap="round"/></svg>Advanced Circuit Training.</li>
    <li><svg viewBox="0 0 30 26"><path d="M2 15 L11 24 C16 12 22 6 29 2" fill="none" stroke="#e3161d" stroke-width="2.4" stroke-linecap="round"/></svg>Advanced Diploma in Personal Training - Level 3 EPRN Registered.</li>
    <li><svg viewBox="0 0 30 26"><path d="M2 15 L11 24 C16 12 22 6 29 2" fill="none" stroke="#e3161d" stroke-width="2.4" stroke-linecap="round"/></svg>Fitness Instructor - Level 2 EPRN Registered.</li>
    <li><svg viewBox="0 0 30 26"><path d="M2 15 L11 24 C16 12 22 6 29 2" fill="none" stroke="#e3161d" stroke-width="2.4" stroke-linecap="round"/></svg>Also qualified in - Suspension training, Studio Cycling, Sports Nutrition, Weight Management.</li>
  </ul>

  <div class="brand-mark">
    <span class="brand-mark__square"></span>
    <span class="brand-mark__name">Corbell Vitality</span>
  </div>
</main>
</body>
</html>
```